Business Card Design Project

We need a double-sided business card design for our e-commerce company. Be as creative as you can.

Reason: Change of logo

Target Market(s)

Business owners

Industry/Entity Type

E-Commerce

Requirements
Must have
• Name (editable)
Mobile number -editable
www.velbiro.com - MUST STAND OUT ALONE
Office address:
27 Marlow Street
#09-04 Westbrook Tower
Singapore 048216

```html
<!DOCTYPE html>
<html lang="en">
<head>
<meta charset="utf-8">
<title>Velbiro Business Card</title>
<link href="https://fonts.googleapis.com/css2?family=Marcellus+SC&family=Josefin+Sans:wght@400&display=swap" rel="stylesheet">
<style>
  :root {
    --stage: #3a3a3a;
    --ink: #111111;
    --paper: #ffffff;
    --mist: #ececec;
    --brand-red: #c4262b;
    --muted: #8a8a8a;
    --text-dark: #1a1a1a;
  }
  * { margin: 0; padding: 0; box-sizing: border-box; }
  html, body { width: 1200px; height: 720px; overflow: hidden; }
  body {
    background: var(--stage);
    position: relative;
    font-family: "Marcellus SC", serif;
  }
  .card {
    position: absolute;
    width: 560px;
    height: 320px;
    border-radius: 24px;
    overflow: hidden;
    box-shadow: 0 14px 30px rgba(0,0,0,0.45);
  }
  .card-front { left: 50px; top: 60px; background: var(--ink); }
  .card-back { left: 590px; top: 340px; background: var(--paper); }
  .card-bg { position: absolute; inset: 0; width: 100%; height: 100%; }

  .brand-name {
    position: absolute;
    font-family: "Marcellus SC", serif;
    color: var(--brand-red);
    line-height: 1;
  }
  .tagline {
    position: absolute;
    font-family: "Josefin Sans", sans-serif;
    color: var(--muted);
    letter-spacing: 0.26em;
    text-transform: uppercase;
    white-space: nowrap;
  }

  .card-front .brand-name { left: 0; width: 480px; top: 96px; text-align: center; font-size: 64px; }
  .card-front .tagline { left: 0; width: 480px; top: 172px; text-align: center; font-size: 15px; }
  .front-web {
    position: absolute; left: 0; width: 480px; top: 200px; text-align: center;
    font-family: "Josefin Sans", sans-serif; font-size: 12px; letter-spacing: 0.2em;
    color: var(--brand-red); text-transform: uppercase;
  }

  .card-back .brand-name { left: 40px; top: 92px; font-size: 54px; }
  .card-back .tagline { left: 44px; top: 156px; font-size: 13px; }
  .holder-name { position: absolute; left: 48px; top: 212px; font-size: 22px; color: var(--text-dark); }
  .holder-title { position: absolute; left: 84px; top: 244px; font-size: 13px; color: var(--text-dark); }

  .address {
    position: absolute; left: 320px; top: 44px;
    font-size: 14px; line-height: 1.25; color: var(--text-dark); font-style: normal;
  }
  .contact-list { position: absolute; left: 376px; top: 118px; list-style: none; }
  .contact-list li {
    display: flex; align-items: center; gap: 12px;
    font-size: 12px; color: var(--text-dark); margin-bottom: 10px;
  }
  .contact-list svg { width: 16px; height: 16px; fill: var(--brand-red); }
</style>
</head>
<body>

  <section class="card card-front" aria-label="Card front">
    <svg class="card-bg" viewBox="0 0 560 320" preserveAspectRatio="none" aria-hidden="true">
      <path d="M560,20 C540,170 300,220 0,290 L0,320 L560,320 Z" fill="var(--mist)"/>
      <path d="M560,110 C500,230 260,260 0,308 L0,320 L560,320 Z" fill="var(--brand-red)"/>
    </svg>
    <div class="brand-name">Velbiro</div>
    <div class="tagline">Everyday Finds Online</div>
    <div class="front-web">www.velbiro.com</div>
  </section>

  <section class="card card-back" aria-label="Card back">
    <svg class="card-bg" viewBox="0 0 560 320" preserveAspectRatio="none" aria-hidden="true">
      <path d="M560,110 C480,230 280,290 120,320 L560,320 Z" fill="var(--ink)"/>
      <path d="M560,140 C490,260 320,300 190,320 L560,320 Z" fill="var(--brand-red)"/>
    </svg>
    <div class="brand-name">Velbiro</div>
    <div class="tagline">Everyday Finds Online</div>
    <div class="holder-name">Name (Editable)</div>
    <div class="holder-title">Your Titel</div>

    <address class="address">
      27 Marlow Street<br>
      #09-04 Westbrook Tower<br>
      Singapore 048216
    </address>

    <ul class="contact-list">
      <li>
        <svg viewBox="0 0 16 16" aria-hidden="true"><path d="M2,6 C2,3 5,2 8,2 C11,2 14,3 14,6 L11,7 L10,5 L6,5 L5,7 Z M4,8 L12,8 L13,14 L3,14 Z"/></svg>
        0000 0000
      </li>
      <li>
        <svg viewBox="0 0 16 16" aria-hidden="true"><circle cx="8" cy="8" r="6.5" fill="none" stroke="var(--brand-red)" stroke-width="1.4"/><path d="M1.5,8 H14.5 M8,1.5 V14.5 M3,4.5 H13 M3,11.5 H13" stroke="var(--brand-red)" stroke-width="1" fill="none"/></svg>
        www.velbiro.com
      </li>
    </ul>
  </section>

</body>
</html>
```